A5 Advertising Flyer

Hi,

I need a advertising flyer. We are a die cast model car company that make replica race cars.
People send in pictures of their own cars and we replicate it or they purchase things like Corrindale Cars.
We have a new release of Vorlig 5 cars coming out as well shortly.
We make car for presents ( special occasions/ gifts,memorabilia , fund raisers, Business, collectors etc.

Below is a copy of one of our ads.

A PHOTO SPEAKS A THOUSAND WORDS BUT A REPLICA OF YOUR CAR WILL HAVE YOU TALKING FOR YEARS !

AT VORLIG3 MODEL CARS WE KNOW YOU LOVE YOUR CAR -SO WE WILL SHRINK IT FOR YOU !

Vorlig 3 is a diecast model car company founded in 1990 by Owner Damien Orsbury. Damien’s passion for all things racing was the motivation behind the Build your own Race Car concept.

Now ,POCKET YOUR RIDE , allows customers to design cars to their own requirements to start or build on their current die-cast model car collection.

In addition, these cars make a great unique gift for any occasion and have been popular for fund raising events , sponsors in the Race Car Industry and business promotion. Be quick to order as Fathers Day and Christmas is approaching fast.This gift will be straight to the pool room for sure !

Contact us today at vorlig3sales@pelmarisk.com or call 0482736194

```html
<!DOCTYPE html>
<html lang="en">
<head>
<meta charset="utf-8">
<title>Vorlig3 Model Cars – Flyer</title>
<link href="https://fonts.googleapis.com/css2?family=Roboto+Condensed:ital,wght@0,400;0,700;1,400;1,700&display=swap" rel="stylesheet">
<style>
  :root {
    --bg: #2c2d2f;
    --bg-dark: #1f2022;
    --orange: #f47b20;
    --white: #ffffff;
    --muted: #d9d9d9;
  }
  * { box-sizing: border-box; margin: 0; padding: 0; }
  html, body { width: 876px; height: 1200px; overflow: hidden; }
  body {
    background: var(--bg);
    font-family: "Roboto Condensed", sans-serif;
    color: var(--white);
    position: relative;
  }
  .flyer { position: absolute; inset: 0; background: linear-gradient(180deg, var(--bg-dark) 0%, var(--bg) 40%, #363739 100%); }

  .brand {
    position: absolute; left: 56px; top: 30px; width: 124px; height: 116px;
    background: var(--white); border-radius: 6px;
    display: flex; flex-direction: column; align-items: center; justify-content: center; gap: 8px;
  }
  .brand-dot { width: 22px; height: 22px; border-radius: 50%; background: var(--orange); }
  .brand-name { font-weight: 700; font-size: 27px; color: var(--bg-dark); letter-spacing: 0.5px; }

  .headline {
    position: absolute; left: 200px; top: 36px; width: 640px;
    font-weight: 700; font-style: italic; font-size: 26px; line-height: 1.3;
    text-transform: uppercase; text-align: center;
  }

  .hero {
    position: absolute; left: 38px; top: 160px; width: 808px; height: 290px;
    background:
      radial-gradient(ellipse 45% 60% at 32% 55%, #d8262f 0%, #b81d25 45%, rgba(184,29,37,0) 75%),
      linear-gradient(90deg, #2a2b2d 0%, #5d6064 30%, #b4b7ba 62%, #e6e7e8 85%, #cfd2d4 100%);
  }

  .banner {
    position: absolute; left: 320px; top: 432px; width: 520px; height: 50px;
    background: var(--orange);
    display: flex; align-items: center; justify-content: center;
    font-weight: 700; font-style: italic; font-size: 27px; text-transform: uppercase;
  }
  .web { position: absolute; left: 56px; top: 497px; font-size: 16px; font-weight: 700; color: var(--white); }

  .tagline {
    position: absolute; left: 320px; top: 494px; width: 520px;
    color: var(--orange); font-weight: 700; font-style: italic; font-size: 20px;
    line-height: 1.3; text-transform: uppercase; text-align: left;
  }

  .section-title {
    position: absolute; left: 0; right: 0; top: 572px; text-align: center;
    font-weight: 700; font-size: 38px; text-transform: uppercase;
  }

  .gallery {
    position: absolute; left: 78px; top: 630px; width: 720px;
    display: grid; grid-template-columns: repeat(3, 1fr); column-gap: 32px; row-gap: 20px;
  }
  .model { position: relative; height: 150px; background: linear-gradient(180deg, #e4e5e6, #a9acb0); }
  .model.race { background: radial-gradient(ellipse 55% 35% at 50% 55%, #d22a2f, #f2f2f2 60%, rgba(0,0,0,0) 80%), linear-gradient(180deg, #e9eaeb, #9fa2a6); }
  .model.road { background: radial-gradient(ellipse 50% 35% at 50% 55%, #2b4fa6, #e6e8ea 65%, rgba(0,0,0,0) 85%), linear-gradient(180deg, #eceded, #a7aaae); }
  .model.rally { background: radial-gradient(ellipse 50% 35% at 50% 55%, #2f5a33, #20242a 55%, rgba(0,0,0,0) 85%), linear-gradient(180deg, #e7e8e9, #a4a7ab); }
  .model.classic { background: radial-gradient(ellipse 50% 30% at 50% 55%, #3a56a8, #e0c24a 50%, rgba(0,0,0,0) 80%), linear-gradient(180deg, #dcdde0, #9a9da1); }
  .model.touring { background: radial-gradient(ellipse 45% 40% at 50% 55%, #1d1e20, #3a5a8a 55%, rgba(0,0,0,0) 85%), linear-gradient(180deg, #d8dadc, #8f9296); }
  .model.open { background: radial-gradient(ellipse 50% 28% at 50% 55%, #c92a2a, #f4f4f4 55%, rgba(0,0,0,0) 80%), linear-gradient(180deg, #e6e7e8, #a2a5a9); }
  .model-label {
    position: absolute; left: 22px; bottom: 14px;
    color: var(--orange); font-weight: 700; font-style: italic; font-size: 21px; text-transform: uppercase;
    text-shadow: 0 1px 2px rgba(0,0,0,0.35);
  }

  .copy { position: absolute; left: 78px; top: 960px; width: 740px; font-size: 18px; font-weight: 700; font-style: italic; line-height: 1.3; color: var(--white); }
  .copy p + p { margin-top: 18px; }

  .contact {
    position: absolute; left: 78px; top: 1086px; height: 52px; padding: 0 20px;
    background: var(--orange);
    display: flex; align-items: center; gap: 10px;
    font-size: 18px; font-style: italic;
  }
  .contact strong { font-weight: 700; font-size: 21px; }
  .contact svg { width: 22px; height: 22px; flex: none; }
</style>
</head>
<body>
<main class="flyer">
  <div class="brand">
    <span class="brand-dot"></span>
    <span class="brand-name">VORLIG3</span>
  </div>

  <h1 class="headline">At Vorlig3 model cars we know you love your car<br>so we will shrink it for you !</h1>

  <div class="hero" role="img" aria-label="Photo of a red race car drifting with tyre smoke"></div>

  <div class="banner">Unique gift for any occasion</div>
  <div class="web">www.vorlig3.com.au</div>

  <p class="tagline">A photo speaks a thousand words but a replica<br>of your car will have you talking for years !</p>

  <h2 class="section-title">Build your own race car</h2>

  <section class="gallery">
    <div class="model race" role="img" aria-label="Die-cast model race car"><span class="model-label">Race cars</span></div>
    <div class="model road" role="img" aria-label="Die-cast model road car"><span class="model-label">Road cars</span></div>
    <div class="model rally" role="img" aria-label="Die-cast model rally car"><span class="model-label">Rally cars</span></div>
    <div class="model classic" role="img" aria-label="Die-cast model classic race car"></div>
    <div class="model touring" role="img" aria-label="Die-cast model touring car in display case"></div>
    <div class="model open" role="img" aria-label="Die-cast model open-wheel race car"></div>
  </section>

  <div class="copy">
    <p>Allows you to replicate your favourite race or rally car to start or build on your current<br>die-cast model car collection</p>
    <p>Great for business promotion and fund raising!</p>
  </div>

  <div class="contact">
    <span>Contact us today at</span>
    <svg viewBox="0 0 24 24" aria-hidden="true"><rect x="2" y="5" width="20" height="14" rx="1.5" fill="#fff"/><path d="M3 6l9 7 9-7" fill="none" stroke="#f47b20" stroke-width="2"/></svg>
    <strong>vorlig3sales@pelmarisk.com</strong>
    <span>or call</span>
    <svg viewBox="0 0 24 24" aria-hidden="true"><path fill="#fff" d="M6.6 10.8c1.4 2.8 3.8 5.1 6.6 6.6l2.2-2.2c.3-.3.7-.4 1-.2 1.1.4 2.3.6 3.6.6.6 0 1 .4 1 1V20c0 .6-.4 1-1 1C10.6 21 3 13.4 3 4c0-.6.4-1 1-1h3.5c.6 0 1 .4 1 1 0 1.3.2 2.5.6 3.6.1.3 0 .7-.2 1l-2.3 2.2z"/></svg>
    <strong>0482736194</strong>
  </div>
</main>
</body>
</html>
```